Wordpress Theme Design for Family Law Firm

Hello, this is a WordPress theme design project, for a "Divorce and Family Law Mediation" practice.

I'd want the wordpress theme to be modeled loosely on this existing design from another one of our own sites: http://www.corvel-debtrelief-guide.example/

We want it to be bright and vibrant and convey a happy and relaxed feeling. The lines on it to not be sharp so more of the rounded edges and subtle shadows that you see on the example site.

Although built on WordPress, the site will be mostly static with fixed content pages, but including a blog feature.

The images will need to be different, but conveying a similar look and feel as the sample site. The colors from the sample site are close to what I'd like - but open to creative options.

It's important that the site looks professional, as well as friendly, and conveys the idea of mediation and relationships.

Important note: Traditional divorce website is for people looking to fight or being bullied.

Divorce mediation is for couples who have decided to split amicably so they're in a much more cooperative state of mind. There's not as much stress and anger. It's just about HOW we go about finalizing the process. There's light at the end of the tunnel.

With that in mind, the site should look friendly and happy, with an inspiring theme of a bright future.

Target Market(s)

The target market are people looking for amicable resolution, with a happy and uplifting attitude..

Traditional divorce websites are for people generally looking to fight or being bullied.

Divorce mediation (this website) is for couples who have decided to split amicably so they're in a much more cooperative state of mind. There's not as much stress and anger. It's just about HOW we go about finalizing the process. There's light at the end of the tunnel.

Industry/Entity Type

Family Law

Requirements
Must have
• Must have option for 1 or two sidebars for pages. This is because some of the internal pages will only have a single sidebar.

The footer will have the option for widgets.

```html
<!DOCTYPE html>
<html lang="en">
<head>
<meta charset="utf-8">
<title>Family Law Mediation</title>
<link rel="stylesheet" href="https://fonts.googleapis.com/css2?family=Fira+Sans:ital,wght@0,400;0,500;1,300&family=Open+Sans:wght@400;600&display=swap">
<style>
:root{
  --navy:#2c3a66;
  --navy-dark:#233058;
  --heading:#283a6e;
  --blue:#2a7cc4;
  --blue-light:#5fb2ec;
  --text:#2b2b2b;
  --muted:#9a9a9a;
  --footer-top:#343434;
  --footer-bottom:#070707;
}
*{margin:0;padding:0;box-sizing:border-box}
html,body{width:993px;height:1200px;overflow:hidden;background:#fff}
.page{position:absolute;left:0;top:0;width:1200px;height:1450px;transform:scale(.8275);transform-origin:0 0;font-family:"Open Sans",sans-serif;color:var(--text)}
.abs{position:absolute}

/* header */
.site-header{left:0;top:0;width:1200px;height:142px;background:linear-gradient(180deg,#fafcfe,#dcecf8)}
.brand-mark{left:121px;top:43px;width:48px;height:48px;background:var(--navy)}
.brand-name{left:181px;top:36px;font:400 36px "Fira Sans",sans-serif;color:var(--heading);white-space:nowrap}
.brand-tagline{left:182px;top:76px;font-size:13px;color:#333}
.call-label{left:892px;top:50px;font:500 21px "Fira Sans",sans-serif;color:var(--blue);letter-spacing:.5px}
.call-number{left:828px;top:70px;font:400 30px "Fira Sans",sans-serif;color:#333;letter-spacing:1.5px}
.call-icon{left:1022px;top:54px}

/* nav */
.main-nav{left:0;top:142px;width:1200px;height:40px;background:var(--navy);display:flex;align-items:center;padding-left:139px}
.main-nav a{color:#fff;text-decoration:none;font-size:12px;height:40px;line-height:40px;padding:0 23px;border-left:1px solid #45527d}
.main-nav a:first-child{border:0;background:linear-gradient(180deg,#4aa3e6,#1f78c4);padding:0 21px}
.main-nav a:nth-child(2){border:0;margin-left:16px;border-left:1px solid #45527d}

/* hero */
.hero{left:0;top:182px;width:1200px;height:323px;background:linear-gradient(180deg,#d9ebf8,#f3f8fc)}
.hero-panel{left:101px;top:0;width:998px;height:323px;background:linear-gradient(90deg,#fff 60%,#f4f9fd);box-shadow:0 0 14px rgba(120,150,180,.35)}
.hero-photo{left:570px;top:182px;width:527px;height:323px;background:linear-gradient(135deg,#e8edf2 0%,#b8cfe4 40%,#4f8fc4 70%,#d8dee5 100%);border-radius:0 0 0 30px}
.hero-title{left:121px;top:250px;font:400 34px "Fira Sans",sans-serif;color:var(--heading);letter-spacing:.3px}
.hero-sub{left:125px;top:297px;font:300 italic 26px "Fira Sans",sans-serif;color:var(--blue)}
.hero-text{left:126px;top:336px;width:380px;font-size:12px;line-height:18px;color:#222}
.slide-dots{left:128px;top:451px;display:flex;gap:5px}
.slide-dots span{width:18px;height:18px;border-radius:50%;background:radial-gradient(circle at 40% 35%,#fff,#b5b5b5);border:1px solid #bbb}
.slide-dots span:first-child{background:radial-gradient(circle,#333 35%,#ddd 45%)}
.learn-more{left:322px;top:440px;width:145px;height:35px;background:#1c1c1c;border-radius:3px;color:#fff;font-size:13px;display:flex;align-items:center;padding-left:13px;gap:10px}
.learn-more i{width:24px;height:24px;border-radius:50%;background:#3c7fb8;display:flex;align-items:center;justify-content:center}
.slide-arrow{top:293px;width:48px;height:48px}

/* feature boxes */
.feature{top:531px;width:312px;height:136px;border-radius:14px;background:linear-gradient(180deg,#fff 40%,#e6e9ee);box-shadow:0 1px 5px rgba(0,0,0,.2);padding:10px 20px}
.feature h3{font:400 21px/24px "Fira Sans",sans-serif;color:var(--heading)}
.feature p{font-size:12.5px;line-height:16px;margin-top:5px;color:#222}
.feature .more{position:absolute;right:34px;bottom:-9px;width:76px;height:22px;border-radius:11px;background:linear-gradient(180deg,#6cbaf0,#1b71c2);color:#fff;font-size:13px;text-align:center;line-height:22px}

/* sidebar */
.sidebar{left:102px;top:722px;width:245px;height:416px;background:var(--navy);border-radius:12px}
.sidebar-title{left:6px;top:5px;width:232px;height:34px;border-radius:10px;background:linear-gradient(180deg,#7cc4f4,#2880cc);color:#fff;font:400 19px/34px "Fira Sans",sans-serif;padding-left:17px;letter-spacing:.5px}
.sidebar ul{position:absolute;left:16px;top:54px;list-style:none}
.sidebar li{color:#fff;font-size:12px;height:28px;padding-left:14px;position:relative}
.sidebar li::before{content:"";position:absolute;left:0;top:4px;border-left:5px solid #fff;border-top:4px solid transparent;border-bottom:4px solid transparent}

/* content */
.content{left:367px;top:728px;width:700px}
.content h2{font:400 21px "Fira Sans",sans-serif;color:var(--heading)}
.content p{font-size:12.5px;line-height:20px;margin-top:10px}
.content p+p{margin-top:20px}
.content h3{font:400 17px "Fira Sans",sans-serif;margin-top:18px;color:#222}
.checklist{list-style:none;margin-top:10px}
.checklist li{font-size:12.5px;height:22px;display:flex;align-items:center;gap:6px}

/* footer */
.site-footer{left:0;top:1168px;width:1200px;height:282px;background:linear-gradient(180deg,var(--footer-top),var(--footer-bottom))}
.footer-col h4{font:400 23px "Fira Sans",sans-serif;color:#fff;letter-spacing:.5px}
.quick-links{list-style:none;margin-top:20px}
.quick-links li{color:#fff;font-size:14px;height:28px;display:flex;align-items:center;gap:16px;letter-spacing:.4px}
.footer-divider{top:1178px;width:1px;height:252px;background:#555}
.services-photo{left:483px;top:1228px;width:278px;height:131px;background:linear-gradient(160deg,#8fb3d6,#5c6f86 50%,#b79070)}
.services-text{left:483px;top:1370px;width:280px;font-size:12px;line-height:18px;color:var(--muted);text-align:justify}
.field{left:826px;width:256px;background:#fff;border-radius:4px;font-size:12.5px;color:#555;padding:7px 7px}
.submit{left:826px;top:1389px;width:122px;height:25px;border-radius:6px;background:linear-gradient(180deg,#eee,#9c9c9c);color:#333;font:500 18px/25px "Fira Sans",sans-serif;text-align:center;letter-spacing:1px}
</style>
</head>
<body>
<div class="page">

  <header class="site-header abs">
    <div class="brand-mark abs"></div>
    <div class="brand-name abs">Family Law Mediation</div>
    <div class="brand-tagline abs">simply dummy text of the printing.</div>
    <div class="call-label abs">Free Call Us</div>
    <div class="call-number abs">123-456-7890</div>
    <svg class="call-icon abs" width="46" height="56" viewBox="0 0 46 56" aria-hidden="true">
      <path d="M36 4c4-2 7 0 8 3 1 4-6 6-9 12s-3 12-1 16c-3 4-10 12-18 14-5 1-8-2-9-4l5-5c2 2 5 2 8 0 6-5 11-14 13-22 1-4 0-8-2-10z" fill="#2a7cc4"/>
      <ellipse cx="16" cy="53" rx="14" ry="2" fill="#c9d6e2"/>
    </svg>
  </header>

  <nav class="main-nav abs">
    <a>Home</a><a>Firm Overview</a><a>Attorney Profile</a><a>Bankruptcy</a><a>Testimonials</a><a>Blog</a><a>Contact Us</a>
  </nav>

  <section class="hero abs">
    <div class="hero-panel abs"></div>
  </section>
  <div class="hero-photo abs" role="img" aria-label="Photo of a couple reviewing papers together at a laptop"></div>
  <svg class="slide-arrow abs" style="left:70px" viewBox="0 0 48 48" aria-hidden="true"><circle cx="24" cy="24" r="21" fill="#fff" stroke="#555" stroke-width="4"/><path d="M28 16l-10 8 10 8z" fill="#222"/></svg>
  <svg class="slide-arrow abs" style="left:1082px" viewBox="0 0 48 48" aria-hidden="true"><circle cx="24" cy="24" r="21" fill="#fff" stroke="#555" stroke-width="4"/><path d="M20 16l10 8-10 8z" fill="#222"/></svg>
  <h1 class="hero-title abs">Lorem Ipsum is simply dummy.</h1>
  <div class="hero-sub abs">Printing and typesetting industry.</div>
  <p class="hero-text abs">Lorem Ipsum is simply dummy text of the printing and typesetting industry. Lorem Ipsum is simply dummy text of the printing and typesetting industry. Lorem Ipsum is simply dummy text of the printing and typesetting industry.Lorem Ipsum is simply.</p>
  <div class="slide-dots abs"><span></span><span></span><span></span><span></span><span></span><span></span><span></span><span></span></div>
  <div class="learn-more abs">LEARN MORE <i><svg width="10" height="10" viewBox="0 0 10 10"><path d="M3 1l4 4-4 4" stroke="#fff" stroke-width="1.5" fill="none"/></svg></i></div>

  <div class="feature abs" style="left:109px"><h3>Lorem Ipsum is that it<br>has a more-or-less normal.</h3><p>Lorem Ipsum is that it has a more-or-less normal to using 'Content here,</p><span class="more">More...</span></div>
  <div class="feature abs" style="left:444px"><h3>Lorem Ipsum is that it<br>has a more-or-less normal.</h3><p>Lorem Ipsum is that it has a more-or-less normal to using 'Content here,</p><span class="more">More...</span></div>
  <div class="feature abs" style="left:778px;padding-top:20px"><h3>How Can We Help?</h3><p>Lorem Ipsum is that it has a more-or-less normal Ipsum is that it has a more-or-less normal to using 'Content here,</p><span class="more">More...</span></div>

  <aside class="sidebar abs">
    <div class="sidebar-title abs">Lorem Ispum text</div>
    <ul>
      <li>Lorem Ispum text</li><li>Lorem Ispum</li><li>Lorem Ispum text</li><li>Lorem Ispum text</li><li>Lorem Ispum text</li><li>Lorem Ispum</li><li>Lorem Ispum text</li><li>Lorem Ispum is Lorem text</li><li>Lorem Ispum text</li><li>Lorem Ispum text</li><li>Lorem Ispum</li><li>Lorem Ispum text</li><li>Lorem Ispum Ispum text</li>
    </ul>
  </aside>

  <main class="content abs">
    <h2>Lorem Ipsum is simply dummy text of the printing.</h2>
    <p>There are many variations of passages of Lorem Ipsum available, but the majority have suffered alteration in some form, by injected humour, or randomised words which don't look even slightly believable. If you are going to use a passage of Lorem Ipsum, you need to be sure there isn't anything embarrassing hidden in the middle of text. All the Lorem Ipsum generators on the Internet tend to repeat.</p>
    <p>Predefined chunks as necessary, making this the first true generator on the Internet. It uses a dictionary of over 200 Latin words, combined with a handful of model sentence structures, to generate Lorem Ipsum which looks reasonable. The generated Lorem Ipsum is therefore always free from repetition, injected humour, or non-characteristic words etc.</p>
    <h3>Making this the first true generator on the Internet.</h3>
    <ul class="checklist">
      <li><svg width="16" height="14" viewBox="0 0 16 14"><path d="M1 8l5 5L15 1" stroke="#2c3a66" stroke-width="3" fill="none"/></svg>Lorem Ipsum has been the industry's standard dummy text ever since.</li>
      <li><svg width="16" height="14" viewBox="0 0 16 14"><path d="M1 8l5 5L15 1" stroke="#2c3a66" stroke-width="3" fill="none"/></svg>Lorem Ipsum has been the industry's standard been the industry's dummy text ever since</li>
      <li><svg width="16" height="14" viewBox="0 0 16 14"><path d="M1 8l5 5L15 1" stroke="#2c3a66" stroke-width="3" fill="none"/></svg>Lorem Ipsum has been the industry's been the industry's been the industry's standard dummy text ever since</li>
      <li><svg width="16" height="14" viewBox="0 0 16 14"><path d="M1 8l5 5L15 1" stroke="#2c3a66" stroke-width="3" fill="none"/></svg>Lorem Ipsum has been the industry's &nbsp;been industry's standard dummy text ever since</li>
      <li><svg width="16" height="14" viewBox="0 0 16 14"><path d="M1 8l5 5L15 1" stroke="#2c3a66" stroke-width="3" fill="none"/></svg>Lorem Ipsum has been the industry's &nbsp;been the industry's standard dummy text ever since</li>
      <li><svg width="16" height="14" viewBox="0 0 16 14"><path d="M1 8l5 5L15 1" stroke="#2c3a66" stroke-width="3" fill="none"/></svg>Lorem Ipsum has been the industry's standard dummy text ever since</li>
    </ul>
  </main>

  <footer class="site-footer abs"></footer>
  <div class="footer-col abs" style="left:148px;top:1186px">
    <h4>Quick Links</h4>
    <ul class="quick-links">
      <li><svg width="16" height="14" viewBox="0 0 16 14"><path d="M2 8l4 4 8-10" stroke="#fff" stroke-width="2.5" fill="none"/></svg>Home</li>
      <li><svg width="16" height="14" viewBox="0 0 16 14"><path d="M2 8l4 4 8-10" stroke="#fff" stroke-width="2.5" fill="none"/></svg>About us</li>
      <li><svg width="16" height="14" viewBox="0 0 16 14"><path d="M2 8l4 4 8-10" stroke="#fff" stroke-width="2.5" fill="none"/></svg>Services</li>
      <li><svg width="16" height="14" viewBox="0 0 16 14"><path d="M2 8l4 4 8-10" stroke="#fff" stroke-width="2.5" fill="none"/></svg>Testimonials</li>
      <li><svg width="16" height="14" viewBox="0 0 16 14"><path d="M2 8l4 4 8-10" stroke="#fff" stroke-width="2.5" fill="none"/></svg>Blog</li>
    </ul>
  </div>
  <div class="footer-divider abs" style="left:451px"></div>
  <div class="footer-divider abs" style="left:792px"></div>
  <div class="footer-col abs" style="left:483px;top:1186px"><h4>Services</h4></div>
  <div class="services-photo abs" role="img" aria-label="Photo of a cheerful group raising hands together in a city plaza"></div>
  <p class="services-text abs">The Renewal Group's Founder, Dana Whitlock shares her insights into various business methodologies,</p>
  <div class="footer-col abs" style="left:823px;top:1186px"><h4>Contact Us</h4></div>
  <div class="field abs" style="top:1228px;height:28px">Name</div>
  <div class="field abs" style="top:1267px;height:28px">Phone</div>
  <div class="field abs" style="top:1310px;height:63px">Tell Us About Tour Case</div>
  <div class="submit abs">Submit</div>

</div>
</body>
</html>
```